Local Flower Farm Needs Business Card Design

I need business cards designed for a flower farm based in Eudora, Kansas.
Business Info:
We are a local cut flower farm located in Eudora, Kansas, founded by Darla Hoffstrom. What started as a passion for agriculture and search for more joy in daily life has blossomed into a small business dedicated to providing the community with beautiful, fresh, and sustainable flowers. We specialize in local, seasonal blooms, ensuring that every petal reflects the care and dedication we pour into our craft. Our mission is to deliver the highest quality flowers directly to our customers through local farmers markets and to florists who share our commitment to sustainability. Join us in celebrating the beauty of nature, one bloom at a time!
Contact Details:
Darla Hoffstrom
Owner
Phone 913-555-0147
Facebook: Lorabelle Quinn Blossoms
Instagram: @LorabelleQuinnBlossoms
Website: LorabelleQuinnBlossoms.example
Target Market(s)
Wholesale to Florists and Direct to Consumer via Farmers Market
Industry/Entity Type
Florist, Farm
Contact Information for Business Card
Name, Contact Info, Logo
Look and feel

```html
<!DOCTYPE html>
<html lang="en">
<head>
<meta charset="utf-8">
<title>Lorabelle Quinn Blossoms – Business Cards</title>
<link href="https://fonts.googleapis.com/css2?family=Playfair+Display:wght@700&family=Poppins:wght@400;500&display=swap" rel="stylesheet">
<style>
  :root {
    --stage: #dcdcdc;
    --card: #0b272d;
    --card-deep: #092229;
    --teal: #12857b;
    --leaf: #0f5f58;
    --white: #ffffff;
    --rule: #9fb4b3;
  }
  * { margin: 0; padding: 0; box-sizing: border-box; }
  html, body { width: 1200px; height: 1200px; overflow: hidden; }
  body {
    background: var(--stage);
    font-family: "Poppins", sans-serif;
    color: var(--white);
    position: relative;
  }
  .card {
    position: absolute;
    top: 149px;
    width: 515px;
    height: 901px;
    background: linear-gradient(180deg, var(--card) 0%, var(--card-deep) 100%);
    overflow: hidden;
  }
  .card--front { left: 58px; }
  .card--back { left: 617px; }

  .floral {
    position: absolute;
    border-radius: 50%;
    filter: blur(6px);
  }
  .floral--front-top {
    left: 200px; top: -20px; width: 330px; height: 330px;
    background: radial-gradient(circle at 60% 40%, rgba(18,133,123,0.55) 0%, rgba(15,95,88,0.35) 45%, rgba(15,95,88,0) 72%);
  }
  .floral--back-bottom {
    left: 285px; top: 670px; width: 260px; height: 260px;
    background: radial-gradient(circle at 60% 60%, rgba(18,133,123,0.5) 0%, rgba(15,95,88,0.3) 45%, rgba(15,95,88,0) 72%);
  }

  .brand-seal {
    position: absolute;
    left: 50%;
    transform: translate(-50%, -50%);
    border: 1px solid var(--white);
    border-radius: 50%;
    display: flex;
    align-items: center;
    justify-content: center;
    text-align: center;
  }
  .brand-seal__name {
    font-family: "Poppins", sans-serif;
    font-weight: 500;
    color: var(--white);
    text-transform: uppercase;
    letter-spacing: 0.12em;
    line-height: 1.35;
  }
  .card--front .brand-seal { top: 534px; width: 276px; height: 276px; }
  .card--front .brand-seal__name { font-size: 22px; }
  .card--back .brand-seal { top: 172px; width: 188px; height: 188px; }
  .card--back .brand-seal__name { font-size: 15px; }

  .front-url {
    position: absolute;
    top: 760px;
    width: 100%;
    text-align: center;
    font-size: 19px;
    letter-spacing: 0.06em;
  }

  .person {
    position: absolute;
    top: 300px;
    width: 100%;
    text-align: center;
  }
  .person__name {
    font-family: "Playfair Display", serif;
    font-weight: 700;
    font-size: 46px;
    color: var(--teal);
    line-height: 1.1;
  }
  .person__title {
    margin-top: 6px;
    display: flex;
    align-items: center;
    justify-content: center;
    gap: 10px;
    font-size: 22px;
    letter-spacing: 0.14em;
  }
  .person__title::before,
  .person__title::after {
    content: "";
    width: 86px;
    height: 1px;
    background: var(--rule);
  }

  .contact-icons {
    position: absolute;
    top: 431px;
    width: 100%;
    display: flex;
    justify-content: center;
    gap: 8px;
  }
  .contact-icons__item {
    width: 26px; height: 26px;
    border-radius: 50%;
    background: var(--teal);
    display: flex; align-items: center; justify-content: center;
  }

  .contact-list {
    position: absolute;
    top: 482px;
    width: 100%;
    list-style: none;
    text-align: center;
    font-size: 20px;
  }
  .contact-list li { height: 45px; line-height: 30px; }
  .contact-list li:first-child { height: 40px; }
</style>
</head>
<body>
  <section class="card card--front" aria-label="Card front">
    <div class="floral floral--front-top" role="img" aria-label="Teal line-drawn flowering branch"></div>
    <div class="brand-seal">
      <span class="brand-seal__name">Lorabelle Quinn<br>Blossoms</span>
    </div>
    <p class="front-url">LorabelleQuinnBlossoms.example</p>
  </section>

  <section class="card card--back" aria-label="Card back">
    <div class="floral floral--back-bottom" role="img" aria-label="Teal line-drawn flowering stems"></div>
    <div class="brand-seal">
      <span class="brand-seal__name">Lorabelle Quinn<br>Blossoms</span>
    </div>

    <div class="person">
      <h1 class="person__name">Darla Hoffstrom</h1>
      <p class="person__title">Owner</p>
    </div>

    <div class="contact-icons">
      <span class="contact-icons__item" aria-label="Phone">
        <svg width="14" height="14" viewBox="0 0 24 24"><path fill="#fff" d="M6.6 10.8a15.1 15.1 0 0 0 6.6 6.6l2.2-2.2a1 1 0 0 1 1-.25 11.4 11.4 0 0 0 3.6.57 1 1 0 0 1 1 1V20a1 1 0 0 1-1 1A17 17 0 0 1 3 4a1 1 0 0 1 1-1h3.5a1 1 0 0 1 1 1c0 1.25.2 2.45.57 3.57a1 1 0 0 1-.25 1z"/></svg>
      </span>
      <span class="contact-icons__item" aria-label="Website">
        <svg width="16" height="16" viewBox="0 0 24 24" fill="none" stroke="#fff" stroke-width="1.6"><circle cx="12" cy="12" r="9"/><ellipse cx="12" cy="12" rx="4" ry="9"/><path d="M3 12h18M4.5 7.5h15M4.5 16.5h15"/></svg>
      </span>
      <span class="contact-icons__item" aria-label="Social page"></span>
      <span class="contact-icons__item" aria-label="Social handle"></span>
    </div>

    <ul class="contact-list">
      <li>913-555-0147</li>
      <li>LorabelleQuinnBlossoms.example</li>
      <li>Lorabelle Quinn Blossoms</li>
      <li>@LorabelleQuinnBlossoms</li>
    </ul>
  </section>
</body>
</html>
```